High-End Medical Center Website Design Project

This design is part of a well thought-out project by an experienced project manager / developer. The approved wireframe is attached. Creative interpretations / suggestions based on the layout encouraged.

The design is for a new state-of-the-art medical center located in Dallas, Texas. The target audience would likely be individuals (approx. 60% female /40% male) who are the healthcare decision-makers for their families. They would likely have insurance and be inclined to seek out top-quality care.

Potential clients would choose this client over others in their industry because the medical center is physician owned, meaning it is patient-focused rather than profit-focused. The facility is brand new, featuring the latest technology. (This includes an amazing waiting room featuring WiFi and docking stations.) The physicians are hand-picked by referral only.

The look of the site should be extremely clean. We are going for a well-organized, professional look with a bit of a warm glow (interpret that however you like). Use crisp corners and the colors in the logo.

Think modern, clean with some great use of color / font.

We can get lovely photography of the medical center once construction is complete. Feel free to use an "example image" behind the Featured Area ("Physician Owned. Patient-Focused") if you like. We are open to ideas.

ONE CHANGE REQUESTED IN THE WIREFRAME:

Remove the "Connect" 1/4 page footer area and replace with a quick contact form. You may swap the "Locations" area with the form if desired. Put social media icons at the top left of the page in the top header area.

(Note: Please use social media icons that match the design rather than standard icons. We preferred not placing the icons at the top, but the client requested this. Let's not bring more attention to them than necessary.)
Updates

We're custom programming this site, so there's no need to base it on a template. Also, we would prefer not to use typical "seen everywhere" stock images.Thanks.

Industry/Entity Type

Construction

Requirements
Must have
• Follow the wireframe. This has been approved.
Nice to have
• Examples of what hover states, links or dropdowns might look like.

```html
<!DOCTYPE html>
<html lang="en">
<head>
<meta charset="utf-8">
<title>Nova Medical Center</title>
<link rel="stylesheet" href="https://fonts.googleapis.com/css2?family=Montserrat:wght@300;600;700&family=Dosis:wght@500;600&family=Arimo:ital,wght@0,400;0,700;1,400&display=swap">
<style>
:root{
  --blue:#0d56a6;
  --blue-dark:#0b4a8a;
  --teal:#3fb0b8;
  --navy:#0f3f78;
  --text:#4a4f57;
  --muted:#7d838b;
  --panel:#eef1f6;
  --line:#d9dee5;
  --white:#ffffff;
}
*{box-sizing:border-box;margin:0;padding:0}
html,body{width:985px;height:1200px;overflow:hidden;background:var(--white)}
body{position:relative;font-family:"Arimo",Arial,sans-serif;color:var(--text)}
.abs{position:absolute}

/* header */
.brand{left:142px;top:18px;height:40px;display:flex;align-items:center;gap:8px;font-family:"Montserrat",sans-serif;font-weight:700;font-size:18px;color:var(--blue);letter-spacing:.5px;white-space:nowrap}
.brand-mark{width:26px;height:26px;background:var(--teal)}
.phone{left:668px;top:10px;display:flex;align-items:center;gap:8px;font-family:"Montserrat",sans-serif;font-weight:600;font-size:20px;color:var(--teal);white-space:nowrap}
.main-nav{left:424px;top:38px;display:flex;height:36px}
.main-nav a{font-family:"Dosis",sans-serif;font-weight:500;font-size:12.5px;letter-spacing:.5px;text-transform:uppercase;color:var(--blue);text-decoration:none;display:flex;align-items:center;justify-content:center;height:36px;white-space:nowrap}
.main-nav a.active{background:var(--blue);color:var(--white);width:80px;position:relative}
.main-nav a.active::after{content:"";position:absolute;bottom:-7px;left:34px;border:6px solid transparent;border-top-color:var(--blue);border-bottom:0}
.main-nav a:hover{color:var(--teal)}
.header-shadow{left:140px;top:74px;width:710px;height:10px;background:radial-gradient(ellipse at top,rgba(0,0,0,.18),transparent 70%)}

/* hero */
.hero-photo{left:0;top:86px;width:985px;height:466px;background:linear-gradient(180deg,#dfe9f3 0%,#9fc0df 30%,#6f9fcf 55%,#c9dbec 75%,#f1f5f9 100%)}
.hero-fade{left:0;top:420px;width:985px;height:132px;background:rgba(255,255,255,.55)}
.banner{left:179px;top:256px;height:62px;display:flex;font-family:"Montserrat",sans-serif;font-size:26px;color:var(--white);white-space:nowrap}
.banner span{display:flex;align-items:center;height:62px}
.banner .light{background:var(--blue);font-weight:300;padding-left:24px;width:311px}
.banner .bold{background:var(--teal);font-weight:700;padding-left:6px;width:310px}

/* features */
.features-title{left:366px;top:392px;width:240px;text-align:center;font-family:"Montserrat",sans-serif;font-weight:600;font-size:15px;color:var(--blue);white-space:nowrap}
.feature-card{top:420px;height:264px;background:rgba(255,255,255,.82)}
.feature-card.center{background:var(--white);box-shadow:0 0 10px rgba(0,0,0,.12)}
.feature-icon{width:124px;height:124px;border-radius:50%;top:416px;display:flex;align-items:center;justify-content:center}
.feature-icon.blue{background:var(--blue)}
.feature-icon.teal{background:var(--teal)}
.feature-name{top:551px;width:240px;text-align:center;font-family:"Montserrat",sans-serif;font-weight:600;font-size:17px;color:var(--navy);white-space:nowrap}
.feature-text{top:580px;width:200px;text-align:center;font-size:9.3px;line-height:13.4px;color:var(--blue-dark)}
.btn{display:flex;align-items:center;justify-content:center;height:21px;border-radius:11px;font-family:"Dosis",sans-serif;font-weight:600;font-size:11.5px;letter-spacing:.8px;text-transform:uppercase;color:var(--white);background:var(--blue);text-decoration:none;box-shadow:0 1px 2px rgba(0,0,0,.3);white-space:nowrap}
.btn.teal{background:var(--teal)}
.btn:hover{background:var(--teal)}
.features-shadow{left:130px;top:684px;width:725px;height:12px;background:radial-gradient(ellipse at top,rgba(0,0,0,.16),transparent 70%)}

/* intro */
.doctor-photo{left:143px;top:732px;width:158px;height:221px;border:4px solid #eceff3;background:linear-gradient(180deg,#f5f7fa,#dde5ee 55%,#c7d3e0)}
.intro-heading{left:320px;top:736px;font-family:"Montserrat",sans-serif;font-weight:600;font-size:19px;color:var(--navy)}
.intro-text{left:320px;top:770px;width:260px;font-size:9.6px;line-height:16.2px;color:var(--muted)}
.intro-text p+p{margin-top:2px}

.testimonials{left:590px;top:713px;width:246px;height:254px;background:var(--panel);border:1px solid var(--line)}
.testimonials h2{position:absolute;left:20px;top:22px;font-family:"Montserrat",sans-serif;font-weight:600;font-size:18px;color:var(--navy)}
.quote{position:absolute;left:20px;width:212px}
.quote .avatar{position:absolute;left:0;top:0;width:36px;height:36px;background:linear-gradient(#c5ccd5,#8d97a3)}
.quote p{margin-left:44px;font-size:10px;line-height:15.6px;color:var(--blue)}
.quote .q{color:#b9c2cc;font-family:"Montserrat",sans-serif;font-weight:700;font-size:13px}
.quote cite{display:block;text-align:right;font-size:9.5px;color:var(--muted);margin-top:4px}
.quote-rule{position:absolute;left:20px;width:206px;height:1px;background:var(--line)}

/* footer widgets */
.footer-area{left:0;top:986px;width:985px;height:172px;border-top:1px solid var(--line);background:linear-gradient(180deg,#ffffff,#eef0f0)}
.footer-col h3{font-family:"Montserrat",sans-serif;font-weight:600;font-size:12.5px;color:var(--blue);text-transform:uppercase;white-space:nowrap}
.footer-col p{font-size:9px;line-height:12px;color:var(--muted)}
.date{left:142px;top:1028px;text-align:center;width:28px;font-family:"Montserrat",sans-serif;color:var(--navy)}
.date b{display:block;font-size:15px;line-height:16px}
.date small{font-size:8px;font-weight:700}
.news-text{font-size:9px;line-height:12px;color:var(--muted)}
.share{display:flex;gap:4px;align-items:center;font-size:8px;color:var(--muted)}
.share i{display:inline-block;width:28px;height:13px;border:1px solid #c3cad3;background:#eef2f7;border-radius:2px}
.share em{font-style:normal;border:1px solid #ccd;padding:0 3px;background:#fff}
.readmore{font-size:9px;font-weight:700;color:var(--blue);text-decoration:none}
.timer{left:504px;top:1026px;width:136px;height:34px;background:var(--blue);color:var(--white);font-family:"Montserrat",sans-serif;font-size:17px;display:flex;align-items:center;justify-content:center;letter-spacing:1px}
.loc-links a{font-size:9px;line-height:12px;color:var(--blue);text-decoration:underline;display:block}
.field{width:172px;height:22px;border:1px solid #d4d7d2;background:linear-gradient(#fff,#ecece6);font-size:9.5px;color:var(--navy);padding:5px 10px;font-family:"Arimo",sans-serif}
.submit{left:778px;top:1100px;width:68px;height:21px}

/* bottom bar */
.bottom-bar{left:0;top:1158px;width:985px;height:42px;background:var(--blue-dark);color:var(--white);font-size:9.5px}
.copyright{position:absolute;left:143px;top:15px;white-space:nowrap}
.socials{position:absolute;left:428px;top:10px;display:flex;gap:4px}
.socials span{width:21px;height:21px;border-radius:50%;background:var(--white)}
.footer-nav{position:absolute;left:558px;top:15px;display:flex;white-space:nowrap}
.footer-nav a{color:var(--white);text-decoration:none;padding:0 6px;border-left:1px solid rgba(255,255,255,.6);line-height:11px}
.footer-nav a:first-child{border-left:0;padding-left:0}
</style>
</head>
<body>

<header>
  <div class="abs brand"><span class="brand-mark"></span>NOVA MEDICAL CENTER</div>
  <div class="abs phone">
    <svg width="20" height="20" viewBox="0 0 24 24" aria-hidden="true"><path fill="#0d56a6" d="M6.6 10.8a15.1 15.1 0 0 0 6.6 6.6l2.2-2.2c.3-.3.7-.4 1-.2 1.1.4 2.3.6 3.6.6.6 0 1 .4 1 1V20c0 .6-.4 1-1 1A17 17 0 0 1 3 4c0-.6.4-1 1-1h3.5c.6 0 1 .4 1 1 0 1.3.2 2.5.6 3.6.1.3 0 .7-.2 1z"/></svg>
    (555) 010-2040
  </div>
  <nav class="abs main-nav">
    <a class="active" href="#">Why Nova</a>
    <a href="#" style="width:82px">Physians</a>
    <a href="#" style="width:86px">Specialist</a>
    <a href="#" style="width:52px">Info</a>
    <a href="#" style="width:86px">Locations</a>
    <a href="#" style="width:60px">Contact</a>
  </nav>
  <div class="abs header-shadow"></div>
</header>

<section>
  <div class="abs hero-photo" role="img" aria-label="Group photo of smiling physicians and nurses in scrubs and white coats"></div>
  <div class="abs hero-fade"></div>
  <h1 class="abs banner"><span class="light">PHYSICIAN OWNED</span><span class="bold">PATIENT FOCUSED</span></h1>
</section>

<section>
  <div class="abs feature-card" style="left:156px;width:220px"></div>
  <div class="abs feature-card center" style="left:378px;width:216px"></div>
  <div class="abs feature-card" style="left:596px;width:244px"></div>
  <h2 class="abs features-title">WHATS SETS US APART</h2>

  <div class="abs feature-icon blue" style="left:203px">
    <svg width="80" height="80" viewBox="0 0 80 80" aria-hidden="true" fill="none" stroke="#fff" stroke-width="4" stroke-linecap="round"><path d="M18 14c-6 6-4 22 8 28s16 8 24 20"/><path d="M30 10c6 8 4 20-4 32"/><circle cx="56" cy="58" r="8"/><circle cx="18" cy="14" r="3" fill="#fff"/><circle cx="30" cy="10" r="3" fill="#fff"/></svg>
  </div>
  <div class="abs feature-icon teal" style="left:424px">
    <svg width="80" height="80" viewBox="0 0 80 80" aria-hidden="true"><g fill="none" stroke="#fff" stroke-width="4"><path d="M28 24a22 22 0 0 1 24 0"/><path d="M58 34a22 22 0 0 1-10 24"/><path d="M32 58a22 22 0 0 1-10-24"/></g><g fill="#fff"><circle cx="40" cy="18" r="9"/><circle cx="60" cy="52" r="9"/><circle cx="20" cy="52" r="9"/></g></svg>
  </div>
  <div class="abs feature-icon blue" style="left:650px">
    <span style="font-family:'Montserrat',sans-serif;font-weight:700;font-size:70px;color:#fff">?</span>
  </div>

  <h3 class="abs feature-name" style="left:150px">TECHNOLOGY</h3>
  <h3 class="abs feature-name" style="left:366px">QUALITY OF CARE</h3>
  <h3 class="abs feature-name" style="left:592px">PATIENT EXPERIENCE</h3>

  <p class="abs feature-text" style="left:170px">Lorem ipsum dolor sit amet, consectetuer adipiscing elit, sed diam nonummy nibh euismod tincidunt ut laoreet dolore magna aliquam erat volutpat. Ut wisi enim ad minim veniam, quis nostrud exerci tation ullamcorper suscipit lobortis nisl ut aliquip ex ea commodo consequat.</p>
  <p class="abs feature-text" style="left:386px">Lorem ipsum dolor sit amet, consectetuer adipiscing elit, sed diam nonummy nibh euismod tincidunt ut laoreet dolore magna aliquam erat volutpat. Ut wisi enim ad minim veniam, quis nostrud exerci tation ullamcorper suscipit lobortis nisl ut aliquip ex ea commodo consequat.</p>
  <p class="abs feature-text" style="left:612px">Lorem ipsum dolor sit amet, consectetuer adipiscing elit, sed diam nonummy nibh euismod tincidunt ut laoreet dolore magna aliquam erat volutpat. Ut wisi enim ad minim veniam, quis nostrud exerci tation ullamcorper suscipit lobortis nisl ut aliquip ex ea commodo consequat.</p>

  <a class="abs btn" href="#" style="left:228px;top:672px;width:84px">Read more</a>
  <a class="abs btn teal" href="#" style="left:441px;top:672px;width:84px">Read more</a>
  <a class="abs btn" href="#" style="left:669px;top:672px;width:84px">Read more</a>
  <div class="abs features-shadow"></div>
</section>

<section>
  <div class="abs doctor-photo" role="img" aria-label="Portrait of a physician in a white coat with arms crossed"></div>
  <h2 class="abs intro-heading">HEADING 1</h2>
  <div class="abs intro-text">
    <p>Lorem ipsum dolor sit amet, consectetuer adipiscing elit, sed diam nonummy nibh euismod tincidunt ut laoreet dolore magna aliquam erat volutpat. Ut wisi enim ad minim veniam, quis nostrud exerci tation ullamcorper suscipit lobortis nisl ut aliquip ex ea commodo consequat.</p>
    <p>Lorem ipsum dolor sit amet, consectetuer adipiscing elit, sed diam nonummy nibh euismod tincidunt ut laoreet dolore magna aliquam erat volutpat. Ut wisi enim ad minim veniam, quis nostrud exerci tation ullamcorper suscipit lobortis nisl ut aliquip ex ea commodo consequat.</p>
  </div>
  <a class="abs btn" href="#" style="left:319px;top:938px;width:84px">Read more</a>

  <aside class="abs testimonials">
    <h2>TESTIMONIALS</h2>
    <div class="quote" style="top:54px">
      <div class="avatar" role="img" aria-label="Photo of a patient"></div>
      <p><span class="q">“ </span>Lorem ipsum dolor sit amet, consectetuer adipiscing elit, sed diam nonummy nibh euismod tincidunt ut laoreet dolore <span class="q">”</span></p>
      <cite>Lena Brooks</cite>
    </div>
    <div class="quote-rule" style="top:132px"></div>
    <div class="quote" style="top:144px">
      <div class="avatar" role="img" aria-label="Photo of a patient"></div>
      <p><span class="q">“ </span>Lorem ipsum dolor sit amet, consectetuer adipiscing elit, sed diam nonummy nibh euismod tincidunt ut laoreet dolore <span class="q">”</span></p>
      <cite>Owen Hartley</cite>
    </div>
    <a class="btn" href="#" style="position:absolute;left:18px;top:222px;width:84px">Read more</a>
  </aside>
</section>

<footer>
  <div class="abs footer-area"></div>

  <div class="abs footer-col" style="left:142px;top:998px;width:165px">
    <h3>News</h3>
  </div>
  <div class="abs date"><b>17</b><small>JAN</small></div>
  <p class="abs news-text" style="left:178px;top:1027px;width:128px">Lorem ipsum dolor sit amet, consectetuer adipiscing elit, sed diam nonummy nibh euismod</p>
  <p class="abs news-text" style="left:142px;top:1064px;width:168px">Lorem ipsum dolor sit amet, consectetuer adipiscing elit, se</p>
  <div class="abs share" style="left:142px;top:1090px"><i></i><em>2.6k</em><span style="width:10px"></span><i></i><em>13</em></div>
  <a class="abs readmore" href="#" style="left:142px;top:1112px">Readmore</a>

  <div class="abs footer-col" style="left:323px;top:998px;width:170px">
    <h3>Blog</h3>
    <p style="margin-top:14px">Lorem ipsum dolor sit amet, consectetuer adipiscing elit, sed diam nonummy nibh euismod</p>
    <p style="margin-top:12px">Lorem ipsum dolor sit amet, consectetuer adipiscing elit, sed diam nonummy nibh euismod</p>
  </div>

  <div class="abs footer-col" style="left:504px;top:998px;width:150px">
    <h3>Average wait time</h3>
  </div>
  <div class="abs timer">00 : 09 : 00</div>
  <div class="abs footer-col" style="left:504px;top:1071px;width:150px">
    <h3>Locations</h3>
  </div>
  <div class="abs loc-links" style="left:505px;top:1094px;width:68px"><a href="#">Lorem ipsum sit amet, conse er adipiscing elit</a></div>
  <div class="abs loc-links" style="left:581px;top:1094px;width:68px"><a href="#">Lorem ipsum sit amet, conse er adipiscing elit</a></div>

  <div class="abs footer-col" style="left:671px;top:998px;width:190px">
    <h3>Register for free here!</h3>
    <p style="margin-top:8px;color:var(--blue)">Lorem ipsum dolor sit amet, consectet</p>
  </div>
  <div class="abs field" style="left:671px;top:1044px">Your Name</div>
  <div class="abs field" style="left:671px;top:1071px">Your Email</div>
  <a class="abs btn submit" href="#" style="background:var(--navy)">Submit</a>

  <div class="abs bottom-bar">
    <span class="copyright">© 2013 | Nova Medical Care All rights reserved</span>
    <div class="socials"><span></span><span></span><span></span><span></span></div>
    <nav class="footer-nav">
      <a href="#">Why Nova</a><a href="#">Physians</a><a href="#">Specialist</a><a href="#">Info</a><a href="#">Locations</a><a href="#">Contact</a>
    </nav>
  </div>
</footer>

</body>
</html>
```